Sophisticated hang tag for Childrens Bibs. A professional look required

We make and sell a boutique line of children's bandana bibs and accessories. Help me refresh our current market image as we grow our business. Emphasis on our existing logo and COMPLETE hang tag design required as it doesn't fit the boutique nature of our products as we look to expand existing lines and market reach. We are now selling bibs in The Linden Childrens hospital and a various retail outlets thus the need for a new market image.

The current logo- I like the bright coloured Tots by Quell writing and would ideally like to keep it or have something just as bright with different vectors. The hangtag needs a complete makeover hence I am looking for a professional designer to help with this.

We sell our children's bibs at a premium price, thus would like a hangtag that looks more sophisticated and modern yet still stands out from the rest and draws people in.

Please see photo of our current hangtag. I have attached as many files as I can think of to assist. The width of the current hang tag is 22.5cm x height 19.5cm but please change the shape and design as you see fit. I also have photos of kids wearing the bibs attached.

Please view style of some of our competitors I have attached. Competitor A is the look I would like you to aim to exceed.
Updates

Project Deadline Extended
Reason: Hi there I want to allow designers who have saved my project more time to send me a design and those that have sent me a design a little more time to update/edit. Please let me know if I can help in any way or provide further feedback. Cheers

Target Market(s)

Mothers looking for stylish boutique children's bibs not run of the mill toweling bibs. Grandparents and friends looking for lovely gifts for new mothers and their babies.

Industry/Entity Type

Boutique

Requirements
Must have
• Our slogan which is 'Stylish bibs for stylish bubs'
• Suits-Newborns to teething toddlers
• Proudly made in Australia or Made with love in Australia
• Care Instructions
• -Machine Washable in cold water
• -Dry Flat in Shade
• -Cool Iron
• 100% Cotton Front, 100% Polyester Fleece Inner
• Have a question or comment? Interested in becoming a Tots by Quell stockist?
• contactus@totsbyquell.example We'd love to hear from you.
• Please make it look more refined and sophisticated, i.e less cartoon/clipart look
• Happy for you to experiment with background colour if it is more visually appealing.
Nice to have
• With a soft cotton front to catch dribbles and everyday spills
• Two sets of press studs providing adjustable sizing
• and a delicate, yet durable fleece backing
• to withstand regular washing
• This bib is certain to grow with your baby
Should not have
• Please don't make the tag cartoon like in any way. The tag shaped like an animal or the logo changed to include animals like giraffes or elephants is great. The use of my photo wearing the bib would look great.
• Background to be white or a faded pattern or background to make the bib the focus.

```html
<!DOCTYPE html>
<html lang="en">
<head>
<meta charset="utf-8">
<title>Tots by Quell – Bib Hang Tag</title>
<link rel="stylesheet" href="https://fonts.googleapis.com/css2?family=Comfortaa:wght@300;400;600&display=swap">
<style>
  :root {
    --backdrop: #e8e3dd;
    --tag: #ffffff;
    --ink: #2b2b2b;
    --ink-soft: #555555;
    --pink: #ec2a7c;
    --blue: #5bc5e6;
    --lime: #9ccb2f;
    --yellow: #fbe04a;
  }
  html, body {
    margin: 0;
    padding: 0;
    width: 1200px;
    height: 1018px;
    overflow: hidden;
    background: var(--backdrop);
  }
  .canvas {
    position: relative;
    width: 1200px;
    height: 1018px;
    font-family: "Comfortaa", sans-serif;
    color: var(--ink);
  }
  .tag-shape { position: absolute; inset: 0; }
  .text {
    position: absolute;
    left: 0;
    width: 1200px;
    text-align: center;
    margin: 0;
  }
  .suits {
    top: 170px;
    font-size: 19px;
    line-height: 24px;
    font-weight: 600;
    color: var(--lime);
  }
  .brand-name {
    top: 300px;
    left: 330px;
    width: 530px;
    font-size: 78px;
    line-height: 100px;
    font-weight: 600;
    color: var(--pink);
    white-space: nowrap;
  }
  .slogan {
    top: 436px;
    font-size: 27px;
    line-height: 32px;
    font-weight: 400;
    letter-spacing: 1px;
    color: var(--ink);
  }
  .description {
    top: 690px;
    left: 270px;
    width: 670px;
    font-size: 15px;
    line-height: 19px;
    font-weight: 300;
    color: var(--ink-soft);
  }
  .fabric {
    top: 765px;
    left: 300px;
    width: 600px;
    font-size: 14px;
    line-height: 19px;
    font-weight: 300;
    color: var(--ink-soft);
  }
  .fabric b { font-weight: 600; color: var(--ink); }
  .contact {
    top: 840px;
    left: 290px;
    width: 620px;
    font-size: 14px;
    line-height: 19.5px;
    font-weight: 300;
    color: var(--ink-soft);
  }
  .contact .email { font-weight: 600; color: var(--ink); }
  .badge {
    position: absolute;
    left: 866px;
    top: 248px;
    width: 146px;
    height: 146px;
    border-radius: 50%;
    background: var(--yellow);
  }
  .badge-text {
    position: absolute;
    left: 862px;
    top: 280px;
    width: 130px;
    text-align: center;
    font-size: 15px;
    line-height: 19px;
    margin: 0;
    color: var(--ink-soft);
    transform: rotate(38deg);
  }
  .illustration {
    position: absolute;
    border-radius: 14px;
  }
  .bird-row {
    left: 368px; top: 478px; width: 462px; height: 58px;
    background: linear-gradient(90deg, var(--yellow), var(--pink), var(--blue), var(--lime), var(--yellow), var(--blue));
    opacity: .55;
  }
  .bird-badge { left: 982px; top: 326px; width: 34px; height: 38px; background: var(--pink); opacity: .6; }
  .bird-desc { left: 196px; top: 686px; width: 64px; height: 58px; background: var(--lime); opacity: .6; }
  .bird-fabric { left: 746px; top: 766px; width: 56px; height: 58px; background: var(--yellow); opacity: .7; }
  .bird-foot { left: 568px; top: 934px; width: 48px; height: 38px; background: var(--blue); opacity: .6; }
  .care-icons { position: absolute; left: 545px; top: 805px; }
  .corner-brand {
    position: absolute;
    left: 880px;
    top: 846px;
    width: 292px;
    margin: 0;
    text-align: right;
    font-size: 40px;
    line-height: 50px;
    font-weight: 600;
    color: var(--pink);
    white-space: nowrap;
  }
  .corner-birds {
    left: 922px; top: 908px; width: 250px; height: 30px;
    background: linear-gradient(90deg, var(--yellow), var(--pink), var(--blue), var(--lime));
    opacity: .55;
  }
</style>
</head>
<body>
<main class="canvas">
  <svg class="tag-shape" width="1200" height="1018" viewBox="0 0 1200 1018" aria-hidden="true">
    <path d="M560 22 L640 22 L1082 272 L1180 560 L640 995 L560 995 L20 560 L118 272 Z"
          fill="var(--tag)" stroke="var(--tag)" stroke-width="36" stroke-linejoin="round"/>
    <path class="hang-hole" d="M572 118 L572 104 Q572 96 580 96 L588 96 A12 12 0 0 1 612 96 L620 96 Q628 96 628 104 L628 118 Z"
          fill="var(--backdrop)"/>
    <g class="strap-slots" fill="var(--backdrop)">
      <polygon points="147,428 161,434 120,594 104,588"/>
      <polygon points="1039,428 1053,434 1096,588 1080,594"/>
    </g>
    <path class="neck-curve" d="M240 466 Q600 830 952 466" fill="none" stroke="#8a8a8a" stroke-width="1.2"/>
  </svg>

  <p class="text suits">newborns to teething toddlers</p>
  <h1 class="text brand-name">Tots by Quell</h1>
  <p class="text slogan">STYLISH BIBS FOR STYLISH BUBS</p>

  <div class="badge"></div>
  <p class="badge-text">Made<br>with love in<br>Australia</p>

  <div class="illustration bird-row" role="img" aria-label="Row of small colourful birds"></div>
  <div class="illustration bird-badge" role="img" aria-label="Small pink bird"></div>
  <div class="illustration bird-desc" role="img" aria-label="Small lime bird"></div>
  <div class="illustration bird-fabric" role="img" aria-label="Small yellow bird"></div>
  <div class="illustration bird-foot" role="img" aria-label="Small blue bird"></div>

  <p class="text description">With a soft cotton front to catch dribbles and everyday spills, 2 sets of press studs providing adjustable sizing, and a delicate yet durable minky fleece backing to withstand regular washing. This bib is certain to grow with your baby :-)</p>

  <p class="text fabric"><b>Front:</b> 100% Cotton<br><b>Back:</b> 100% Polyester Minky Fleece</p>

  <svg class="care-icons" width="112" height="28" viewBox="0 0 112 28" role="img" aria-label="Care: cold machine wash, cool iron, dry flat">
    <g fill="none" stroke="#555" stroke-width="1.4">
      <path d="M2 6 L6 24 L30 24 L34 6"/><path d="M2 6 Q8 10 14 6 Q20 10 26 6 Q30 9 34 6"/>
      <path d="M44 24 L76 24 L76 10 L56 10 Q46 12 44 24 Z"/>
      <rect x="86" y="4" width="20" height="20"/><line x1="86" y1="14" x2="106" y2="14"/>
    </g>
    <circle cx="18" cy="16" r="1.8" fill="#555"/><circle cx="62" cy="18" r="1.6" fill="#555"/>
  </svg>

  <p class="text contact">Have a question or comment?<br>Intersted in becoming totsbyquell stockist?<br>We'd love to hear from you!<br><span class="email">contactus@totsbyquell.example</span></p>

  <p class="corner-brand">Tots by Quell</p>
  <div class="illustration corner-birds" role="img" aria-label="Row of small colourful birds"></div>
</main>
</body>
</html>
```